Drinking Game needs a revamped look!

** Please note we are looking for a redesign of the actual game board, not a poster about the game. I chose poster because it was the closest description of what we need. If you have questions, please ask prior to starting.

We need a new look for our Tip Tumble drinking game. I have attached the old tired graphic we use for our games. We want to liven it up a bit! Along with revamping the current look of the game we are also adding Tip "a wee" tumble as a cheaper alternative. We will need a design for that as well. Both can be about the same size of about 11.5x17.5". The difference on the tip a wee tumble will be one less number and one less letter so A-I and 1-7.

I have also attached our current logo which I would like incorporated in the design as well as our site TipTumble.com.
Updates

Target Market(s)

Drinkers and game players :-)

Requirements
Must have
• A hot new look that stands out from stained wood. You can see the current product at www.tiptumble.com.

```html
<!DOCTYPE html>
<html lang="en">
<head>
<meta charset="utf-8">
<title>Tip Tumble – Game Board</title>
<link href="https://fonts.googleapis.com/css2?family=Questrial&family=Michroma&display=swap" rel="stylesheet">
<style>
  :root {
    --backdrop: #2e2219;
    --board: #000000;
    --lime: #c4df3a;
    --cell-light: #a4c21a;
    --shade: rgba(24, 34, 0, 0.5);
    --ink: #0a0a0a;
  }
  html, body {
    margin: 0;
    padding: 0;
    width: 1200px;
    height: 849px;
    overflow: hidden;
    background: var(--backdrop);
  }
  .board {
    position: absolute;
    left: 55px;
    top: 52px;
    width: 1090px;
    height: 743px;
    background: var(--board);
    font-family: "Questrial", sans-serif;
  }
  .brand {
    position: absolute;
    left: 60px;
    top: 31px;
    width: 80px;
    height: 80px;
    border-radius: 50%;
    background: var(--lime);
    display: flex;
    align-items: center;
    justify-content: center;
    text-align: center;
  }
  .brand-name {
    color: var(--ink);
    font-size: 16px;
    line-height: 1.05;
  }
  .col-heads {
    position: absolute;
    left: 147px;
    top: 53px;
    width: 888px;
    height: 67px;
    display: grid;
    grid-template-columns: repeat(10, 1fr);
    column-gap: 4px;
  }
  .row-heads {
    position: absolute;
    left: 57px;
    top: 123px;
    width: 85px;
    height: 567px;
    display: grid;
    grid-template-rows: repeat(8, 1fr);
    row-gap: 4px;
  }
  .head {
    background: var(--lime);
    color: var(--ink);
    display: flex;
    align-items: center;
    justify-content: center;
    font-size: 34px;
  }
  .grid {
    position: absolute;
    left: 147px;
    top: 123px;
    width: 888px;
    height: 567px;
  }
  .grid svg { display: block; }
  .site {
    position: absolute;
    right: 55px;
    top: 700px;
    color: var(--lime);
    font-family: "Michroma", sans-serif;
    font-size: 21px;
    letter-spacing: 3px;
  }
</style>
</head>
<body>
  <main class="board">
    <div class="brand"><span class="brand-name">Tip<br>Tumble</span></div>

    <div class="col-heads">
      <div class="head">A</div><div class="head">B</div><div class="head">C</div><div class="head">D</div><div class="head">E</div>
      <div class="head">F</div><div class="head">G</div><div class="head">H</div><div class="head">I</div><div class="head">J</div>
    </div>

    <div class="row-heads">
      <div class="head">1</div><div class="head">2</div><div class="head">3</div><div class="head">4</div>
      <div class="head">5</div><div class="head">6</div><div class="head">7</div><div class="head">8</div>
    </div>

    <div class="grid">
      <svg width="888" height="567" viewBox="0 0 888 567">
        <defs>
          <radialGradient id="map-glow" cx="45%" cy="40%" r="55%">
            <stop offset="0%" stop-color="#d6f048" stop-opacity="0.3"/>
            <stop offset="100%" stop-color="#d6f048" stop-opacity="0"/>
          </radialGradient>
        </defs>
        <rect class="grid-base" width="888" height="567" fill="var(--cell-light)"/>
        <g class="row-shades" fill="var(--shade)">
          <rect x="0" y="70.9" width="888" height="70.9"/>
          <rect x="0" y="212.6" width="888" height="70.9"/>
          <rect x="0" y="354.4" width="888" height="70.9"/>
          <rect x="0" y="496.1" width="888" height="70.9"/>
        </g>
        <g class="col-shades" fill="var(--shade)">
          <rect x="88.8" y="0" width="88.8" height="567"/>
          <rect x="266.4" y="0" width="88.8" height="567"/>
          <rect x="444" y="0" width="88.8" height="567"/>
          <rect x="621.6" y="0" width="88.8" height="567"/>
          <rect x="799.2" y="0" width="88.8" height="567"/>
        </g>
        <rect class="world-map" role="img" aria-label="Faint world map silhouette across the game grid" width="888" height="567" fill="url(#map-glow)"/>
      </svg>
    </div>

    <div class="site">TipTumble.com</div>
  </main>
</body>
</html>
```